San Antonio Texas Based Law Firm Needs Eye Catching Professional website

The Calloway Law Firm, PLLC is in need of a fresh, eye catching website that makes the small firm look and appear as professional, organized and innovative as possible.

The Firm wants to highlight its expertise in three main areas.
Estate Planning, Insurance and Mediation.

It is a small firm - but growing, so I am looking for the website to have the appearance not of a small firm - but more of the appearance of a leading national firm. The firm was built after obtaining extensive experience working in both private practice and at two Meridian 400 companies.

The firm was formed based on strong relationships and reputation in the industries the Firm serves and and in the local communities.

My logo, which was designed by pixel forge is clever and something I want to make prominent and build from.

Industry/Entity Type

Legal

Coding

Coded - Design and coding required

Number of Pages Required

3 page

Colors
ffffff
000000

Requirements
Must have
• Very good quality pictures.
• Very organized.
• Easy to navigate.
• A contact Us Page.
• On the Estate Planning page, a place for an upcoming seminar sign up - where we
• would get potential client information to mail out confirmation.
• A way to have people subscribe to periodic updates.
• Link to The Calloway Law Firm Chatterly
• A way to download vcard.
Should not have
• Any pictures of gavels, pillars or other common pictures related to law. (Too boring)

```html
<!DOCTYPE html>
<html lang="en">
<head>
<meta charset="utf-8">
<title>The Calloway Law Firm, PLLC</title>
<link href="https://fonts.googleapis.com/css2?family=PT+Sans:wght@400;700&display=swap" rel="stylesheet">
<style>
:root{
  --backdrop:#1e1e1e;
  --black:#000;
  --ink:#111;
  --tile-a:#0b0b0b;
  --tile-b:#151515;
  --white:#fff;
  --paper:#f2f2f2;
  --grey:#7a7a7a;
  --mid:#555;
  --button:#333;
  --bar:#3a3a3a;
}
*{box-sizing:border-box;margin:0;padding:0}
html,body{width:1200px;height:1200px;overflow:hidden;background:var(--backdrop);font-family:"PT Sans",Arial,sans-serif}
.page{position:absolute;left:319px;top:0;width:563px;height:1200px;background:var(--white)}
.abs{position:absolute}
.topbar{left:0;top:0;width:563px;height:18px;background:var(--black);color:var(--white);font-size:6px}
.topbar .item{position:absolute;top:4px;display:flex;align-items:center;gap:6px}
.topbar .divider{position:absolute;left:125px;top:3px;width:1px;height:12px;background:#666}
.social{display:flex;gap:7px;align-items:center}
.social span{display:block;width:7px;height:7px;border-radius:50%;background:#bbb}
.topbar .social{position:absolute;left:425px;top:5px}
.header{left:0;top:18px;width:563px;height:59px;background:var(--white)}
.logo{position:absolute;left:43px;top:0;width:75px;height:53px;background:var(--black);color:var(--white);display:flex;align-items:center;justify-content:center;text-align:center;font-size:7px;letter-spacing:.5px;line-height:1.35;padding:6px}
.nav{position:absolute;top:26px;font-size:6.2px;font-weight:700;color:var(--ink)}
.nav.active{color:#999;font-weight:400}
.hero{left:0;top:77px;width:563px;height:189px;background:linear-gradient(90deg,#b48a58 0%,#d4b184 28%,#8a8884 52%,#4a4a4a 70%,#9a9a9a 85%,#222 100%)}
.hero .arrow{position:absolute;top:84px}
.dots{position:absolute;display:flex;gap:5px}
.dots span{width:4px;height:4px;border-radius:50%;background:rgba(255,255,255,.55)}
.dots span.on{background:#fff}
.services{left:0;top:266px;width:563px;height:98px;display:flex}
.service{flex:1;display:flex;flex-direction:column;align-items:center;justify-content:flex-start;padding-top:26px;color:var(--white);font-size:9.5px;letter-spacing:.3px}
.service:nth-child(odd){background:var(--tile-a)}
.service:nth-child(2){background:var(--tile-b)}
.service svg{height:30px;margin-bottom:9px}
h2{font-weight:700;color:var(--ink)}
.section-title{position:absolute;left:43px;font-size:18px}
.rule{position:absolute;height:2.5px;background:var(--ink)}
.about-text{left:43px;top:439px;width:196px;font-size:5.3px;font-weight:700;color:var(--grey);line-height:8.8px}
.about-text p+p{margin-top:8.8px}
.btn{left:43px;top:560px;width:84px;height:24px;border-radius:5px;background:var(--button);color:var(--white);font-size:6.8px;display:flex;align-items:center;justify-content:center}
.about-photo{left:281px;top:363px;width:282px;height:220px;background:linear-gradient(90deg,#7a2e1c 0%,#9a4a2c 35%,#5a5048 60%,#3c3c3e 100%)}
.blog{left:0;top:608px;width:563px;height:234px;background:var(--paper)}
.post{position:absolute;width:240px;height:60px}
.thumb{position:absolute;left:0;top:0;width:50px;height:47px}
.post h3{position:absolute;left:62px;top:0;font-size:7px;font-weight:700;color:var(--ink)}
.post p{position:absolute;left:62px;top:11px;width:150px;font-size:5px;font-weight:700;color:var(--grey);line-height:8.7px}
.post .more{position:absolute;right:0;top:53px;font-size:5.3px;font-weight:700;color:var(--ink)}
.testimonial{left:0;top:842px;width:563px;height:196px;text-align:center}
.testimonial h2{position:absolute;left:0;width:563px;top:14px;font-size:17px}
.avatar{position:absolute;left:264px;top:61px;width:34px;height:34px;border-radius:50%;background:linear-gradient(#d8b89a,#a98a70)}
.quote{position:absolute;left:140px;width:283px;top:108px;font-size:6.6px;color:var(--grey);line-height:8.8px}
.client{position:absolute;left:0;width:563px;top:140px;font-size:7px;color:var(--ink)}
.client-co{position:absolute;left:0;width:563px;top:153px;font-size:4.6px;color:#999}
.footer{left:0;top:1038px;width:563px;height:136px;background:var(--black);color:var(--white)}
.footer h4{position:absolute;top:20px;font-size:6.2px;font-weight:400;letter-spacing:.2px}
.contact-row{position:absolute;left:45px;display:flex;gap:7px;font-size:5.3px;line-height:7.5px;align-items:flex-start}
.links{position:absolute;left:185px;top:44px;list-style:none;font-size:4.8px;line-height:10.3px;color:#ddd}
.news-text{position:absolute;left:287px;top:51px;width:120px;font-size:5.3px;line-height:10px}
.email-field{position:absolute;left:288px;top:72px;width:106px;height:15px;background:var(--white);color:#444;font-size:5px;padding-left:5px;display:flex;align-items:center}
.subscribe{position:absolute;left:288px;top:96px;width:106px;height:16px;background:var(--button);font-size:5.3px;display:flex;align-items:center;justify-content:center}
.footer .social{position:absolute;left:432px;top:50px;gap:9px}
.copyright{left:0;top:1174px;width:563px;height:26px;background:var(--bar);color:#ccc;font-size:5.5px;display:flex;align-items:center;justify-content:center}
</style>
</head>
<body>
<div class="page">

  <div class="abs topbar">
    <div class="item" style="left:46px">
      <svg width="9" height="7" viewBox="0 0 9 7"><rect x=".5" y=".5" width="8" height="6" fill="none" stroke="#fff"/><path d="M.5 .5 4.5 4 8.5 .5" fill="none" stroke="#fff"/></svg>
      hello@callowaylaw.example
    </div>
    <div class="divider"></div>
    <div class="item" style="left:138px">
      <svg width="8" height="8" viewBox="0 0 8 8"><path d="M1.5 .5 3 2.5 2 3.5c.6 1.2 1.3 1.9 2.5 2.5l1-1 2 1.5-1 1.2C3.5 7.5.5 4.5.3 1.5Z" fill="#fff"/></svg>
      +1 210 555 0148
    </div>
    <div class="social" role="img" aria-label="Social links including Chatterly"><span></span><span></span><span></span><span></span><span></span><span></span></div>
  </div>

  <div class="abs header">
    <div class="logo">THE CALLOWAY<br>LAW FIRM</div>
    <span class="nav active" style="left:206px">HOME</span>
    <span class="nav" style="left:242px">ABOUT US</span>
    <span class="nav" style="left:288px">ESTATE PLANNING</span>
    <span class="nav" style="left:358px">INSURANCE</span>
    <span class="nav" style="left:408px">MEDIATION</span>
    <span class="nav" style="left:458px">BLOG</span>
    <span class="nav" style="left:491px">CONTACT</span>
  </div>

  <div class="abs hero" role="img" aria-label="Banner photo: living trust and estate planning document with fountain pen, chess pieces, and a gloved hand holding an invitation card">
    <svg class="arrow" style="left:22px" width="8" height="16" viewBox="0 0 8 16"><path d="M7 1 1 8l6 7" fill="none" stroke="#fff" stroke-width="1.5"/></svg>
    <svg class="arrow" style="left:534px" width="8" height="16" viewBox="0 0 8 16"><path d="M1 1l6 7-6 7" fill="none" stroke="#fff" stroke-width="1.5"/></svg>
    <div class="dots" style="left:270px;top:172px"><span class="on"></span><span></span><span></span></div>
  </div>

  <div class="abs services">
    <div class="service">
      <svg viewBox="0 0 26 30" width="26"><rect x="5" y="3" width="16" height="24" fill="none" stroke="#fff" stroke-width="2"/><path d="M2 2l8 8" stroke="#fff" stroke-width="2"/><path d="M9 12h8M9 16h8M9 20h6" stroke="#fff" stroke-width="1.5"/></svg>
      ESTATE PLANNING
    </div>
    <div class="service">
      <svg viewBox="0 0 34 30" width="34"><path d="M17 3 5 14h4v8h16v-8h4Z" fill="none" stroke="#fff" stroke-width="2.5"/><rect x="14" y="15" width="6" height="7" fill="#fff"/><path d="M2 18c2 6 6 9 12 10M32 18c-2 6-6 9-12 10" fill="none" stroke="#fff" stroke-width="3"/></svg>
      INSURANCE
    </div>
    <div class="service">
      <svg viewBox="0 0 30 30" width="30"><circle cx="15" cy="6" r="4" fill="#fff"/><path d="M8 13h14l5 14H3Z" fill="#fff"/><path d="M15 14v12" stroke="#0b0b0b" stroke-width="2"/></svg>
      MEDIATION
    </div>
  </div>

  <h2 class="section-title" style="top:383px">ABOUT US</h2>
  <div class="rule" style="left:43px;top:412px;width:56px"></div>
  <div class="abs about-text">
    <p>Lorem ipsum dolor sit amet, consectetur adipiscing elit. Mauris porta neque libero, nec fringilla felis ornare et. Vestibulum pellentesque, orci sit amet ultrices porta, ipsum tellus sollicitudin dui, varius tincidunt erat purus in dui. Suspendisse id lorem mollis, hendrerit diam sed, vestib ulum neque. Pellentesque id dolor non ante accumsan hendrerit hendrerit sed tellus.</p>
    <p>Nulla rutrum, ex eu facilisis posuere, sem ante aliquet leo, vitae dictum dolor dolor vel augue. Phasellus consectetur dolor dolor, sed imperdiet metus ultricies vitae.</p>
  </div>
  <div class="abs btn">READ MORE</div>
  <div class="abs about-photo" role="img" aria-label="Portrait of an attorney in a grey suit seated in front of law library shelves"></div>

  <div class="abs blog">
    <h2 class="section-title" style="top:30px">BLOG</h2>
    <div class="rule" style="left:43px;top:60px;width:56px"></div>

    <div class="post" style="left:43px;top:80px">
      <div class="thumb" role="img" aria-label="Black and white photo of a handshake" style="background:linear-gradient(135deg,#ddd,#555)"></div>
      <h3>LOREM IPSUM DOLOR SIT AME</h3>
      <p>Lorem ipsum dolor sit amet, consectetur adipiscing elit Suspendisse porta lacus sed leo bibendum, ut lacinia quam molestie.</p>
      <span class="more">READ MORE &gt;&gt;</span>
    </div>
    <div class="post" style="left:287px;top:80px;width:231px">
      <div class="thumb" role="img" aria-label="Photo of an attorney in front of book shelves" style="background:linear-gradient(90deg,#8a3a22,#4a4448)"></div>
      <h3>LOREM IPSUM DOLOR SIT AME</h3>
      <p>Lorem ipsum dolor sit amet, consectetur adipiscing elit Suspendisse porta lacus sed leo bibendum, ut lacinia quam molestie.</p>
      <span class="more">READ MORE &gt;&gt;</span>
    </div>
    <div class="post" style="left:43px;top:144px">
      <div class="thumb" role="img" aria-label="Photo of a will and testament document with a pen" style="background:linear-gradient(135deg,#e8c48a,#b07a3a)"></div>
      <h3>LOREM IPSUM DOLOR SIT AME</h3>
      <p>Lorem ipsum dolor sit amet, consectetur adipiscing elit Suspendisse porta lacus sed leo bibendum, ut lacinia quam molestie.</p>
      <span class="more">READ MORE &gt;&gt;</span>
    </div>
    <div class="post" style="left:287px;top:144px;width:231px">
      <div class="thumb" role="img" aria-label="Photo of hands holding a paper chain of family figures" style="background:linear-gradient(135deg,#c8604a,#e8c8b8)"></div>
      <h3>LOREM IPSUM DOLOR SIT AME</h3>
      <p>Lorem ipsum dolor sit amet, consectetur adipiscing elit Suspendisse porta lacus sed leo bibendum, ut lacinia quam molestie.</p>
      <span class="more">READ MORE &gt;&gt;</span>
    </div>
  </div>

  <div class="abs testimonial">
    <h2>Our Happy client</h2>
    <div class="rule" style="left:252px;top:43px;width:58px"></div>
    <div class="avatar" role="img" aria-label="Client portrait photo"></div>
    <p class="quote">I have found the team to be responsive, knowledgeable and helpful. No question I had was too silly to ask.</p>
    <p class="client">Marisa Whitfield</p>
    <p class="client-co">NorthPeak</p>
    <div class="dots" style="left:270px;top:173px"><span style="background:#ddd"></span><span style="background:#eee"></span><span style="background:#bbb"></span></div>
  </div>

  <div class="abs footer">
    <h4 style="left:45px">CONTACTS</h4>
    <h4 style="left:185px">QUICK LINKS</h4>
    <h4 style="left:289px">NEWSLETTER</h4>
    <h4 style="left:434px">FOLLOW US</h4>

    <div class="contact-row" style="top:47px">
      <svg width="6" height="8" viewBox="0 0 6 8"><path d="M3 0a3 3 0 0 1 3 3c0 2-3 5-3 5S0 5 0 3a3 3 0 0 1 3-3Z" fill="#fff"/><circle cx="3" cy="3" r="1.1" fill="#000"/></svg>
      <span>2480 Alder Crest Blvd, Suite B<br>San Antonio, Texas 78209</span>
    </div>
    <div class="contact-row" style="top:77px">
      <svg width="7" height="7" viewBox="0 0 8 8"><path d="M1.5 .5 3 2.5 2 3.5c.6 1.2 1.3 1.9 2.5 2.5l1-1 2 1.5-1 1.2C3.5 7.5.5 4.5.3 1.5Z" fill="#fff"/></svg>
      <span>1-800-555-0192</span>
    </div>
    <div class="contact-row" style="top:101px">
      <svg width="7" height="7" viewBox="0 0 7 7"><rect x="1.5" y="0" width="4" height="2" fill="#fff"/><rect x="0" y="2.5" width="7" height="3" fill="#fff"/><rect x="1.5" y="5" width="4" height="2" fill="#fff"/></svg>
      <span>1-210-555-0176</span>
    </div>

    <ul class="links">
      <li>HOME</li><li>ABOUT US</li><li>ESTATE PLANNING</li><li>INSURANCE</li><li>MEDIATION</li><li>BLOG</li><li>CONTACT</li>
    </ul>

    <p class="news-text">Enter your e-mail and subscribe to our newsletter</p>
    <div class="email-field">E - mail</div>
    <div class="subscribe">SUBSCRIBE</div>

    <div class="social" role="img" aria-label="Social links including Chatterly"><span></span><span></span><span></span><span></span><span></span><span></span></div>
  </div>

  <div class="abs copyright">Copyright © LAW FIRM. All Rights Reserved</div>
</div>
</body>
</html>
```